Coffee Pouch Label for Coffee Roaster

We are wanting some new labels for our coffee pouches.
We are an established, small family owned specialty coffee roaster called Tallow Creek Coffee Roasters, and we are located in Bellwood, NSW Australia.
Label dimensions are 100 x 150mm, to fit on a couple of different bag sizes. We use coffee pouches with kraft paper finish.
We have 3 main blends, Marigold, Lanternfly & Slow Tide, and a range of rotating single origin coffees. We would get labels printed for the blends, but then need a 'generic' design that we can either write the name on, or stick another sticker over for the single origin coffees.
Some information that needs to be on the label:
our logo
web address: www.tallowcreekcoffee.example
address: 47 Garrick St, Bellwood, NSW
Proudly Roasted in Bellwood, NSW
Blend name
our tagline/mission: Roast Kindly | Share Freely | Stay Curious
statement: we give $1 from every kg of coffee sold to the rescue, prevention and rehabilitation of children from slavery.
We would like to use colour to help differentiate the different blends somehow.
We are after a creative, clean design, that is representative of specialty coffee (not large commercial coffee brands).
I have uploaded our logo both with and without our tagline, and also some other packaging inspiration that i like (I quite like the meadow coffee label design).
thanks everyone!
Rupert
People who appreciate good, local coffee

```html
<!DOCTYPE html>
<html lang="en">
<head>
<meta charset="utf-8">
<title>Tallow Creek Coffee Roasters – Blend Labels</title>
<link rel="stylesheet" href="https://fonts.googleapis.com/css2?family=Oswald:wght@400;600;700&family=Open+Sans:wght@400;600&display=swap">
<style>
  :root {
    --page: #ffffff;
    --ink: #2a2826;
    --label: #ffffff;
    --band: #efe8dc;
    --marigold: #e6dccf;
    --lanternfly: #bdb294;
    --slowtide: #9b7f63;
  }
  * { box-sizing: border-box; margin: 0; padding: 0; }
  html, body {
    width: 1200px; height: 1000px; overflow: hidden;
    background: var(--page);
  }
  .range { position: relative; width: 1200px; height: 1000px; }
  .label {
    position: absolute; top: 252px;
    width: 265px; height: 397px;
    background: var(--label);
    overflow: hidden;
    color: var(--ink);
    box-shadow: 0 0 0 1px rgba(0,0,0,0.06);
  }
  .label--marigold { left: 82px; --tone: var(--marigold); }
  .label--lanternfly { left: 456px; --tone: var(--lanternfly); }
  .label--slowtide { left: 833px; --tone: var(--slowtide); }

  .label__tone {
    position: absolute; left: 34px; top: 0;
    width: 231px; height: 330px;
    background: var(--tone);
  }

  .donation {
    position: absolute; top: 14px; right: 12px; width: 66px;
    text-align: right;
  }
  .donation__badge {
    display: inline-flex; align-items: center; justify-content: center;
    width: 30px; height: 30px; border-radius: 50%;
    background: var(--ink); color: var(--label);
    font-family: "Oswald", sans-serif; font-weight: 400; font-size: 17px;
    margin-right: 8px;
  }
  .donation__text {
    margin-top: 5px;
    font-family: "Open Sans", sans-serif; font-weight: 600;
    font-size: 6.4px; line-height: 1.4;
  }

  .brand__name {
    position: absolute; left: 16px; top: 156px;
    font-family: "Oswald", sans-serif; font-weight: 700;
    font-size: 38px; line-height: 1; letter-spacing: 0.5px;
    text-transform: uppercase; color: var(--ink); white-space: nowrap;
  }
  .brand__trade {
    position: absolute; left: 77px; top: 204px;
    font-family: "Oswald", sans-serif; font-weight: 700;
    font-size: 9px; line-height: 1; letter-spacing: 2.2px;
    text-transform: uppercase; color: var(--ink);
  }

  .tagline {
    position: absolute; left: 20px; top: 218px;
    font-family: "Open Sans", sans-serif; font-weight: 400;
    font-size: 8.4px; line-height: 1; color: var(--ink); white-space: nowrap;
  }

  .blend {
    position: absolute; left: 0; top: 267px;
    width: 208px; height: 26px;
    background: var(--band);
    padding-left: 15px;
    font-family: "Oswald", sans-serif; font-weight: 600;
    font-size: 18px; line-height: 26px;
    letter-spacing: 5.5px; text-transform: uppercase;
    color: var(--ink); white-space: nowrap;
  }

  .footer {
    position: absolute; left: 12px; top: 366px;
    font-family: "Oswald", sans-serif; text-transform: uppercase;
    color: var(--ink); white-space: nowrap;
  }
  .footer__contact { font-weight: 600; font-size: 7px; letter-spacing: 0.4px; line-height: 1; }
  .footer__origin {
    margin-top: 6px; font-weight: 400; font-style: italic;
    font-size: 7px; letter-spacing: 2.6px; line-height: 1;
  }
</style>
</head>
<body>
<main class="range">

  <article class="label label--marigold">
    <div class="label__tone"></div>
    <div class="donation">
      <span class="donation__badge">$1</span>
      <p class="donation__text">donated from every kg of coffee sold to fund schooling and safe homes for children in need.</p>
    </div>
    <h1 class="brand"><span class="brand__name">Tallow Creek</span><span class="brand__trade">Coffee Roasters</span></h1>
    <p class="tagline">Roast Kindly | Share Freely | Stay Curious</p>
    <h2 class="blend">Marigold</h2>
    <div class="footer">
      <p class="footer__contact">tallowcreekcoffee.example | 47 Garrick St, Bellwood, NSW</p>
      <p class="footer__origin">Proudly roasted in Bellwood, NSW</p>
    </div>
  </article>

  <article class="label label--lanternfly">
    <div class="label__tone"></div>
    <div class="donation">
      <span class="donation__badge">$1</span>
      <p class="donation__text">donated from every kg of coffee sold to fund schooling and safe homes for children in need.</p>
    </div>
    <h1 class="brand"><span class="brand__name">Tallow Creek</span><span class="brand__trade">Coffee Roasters</span></h1>
    <p class="tagline">Roast Kindly | Share Freely | Stay Curious</p>
    <h2 class="blend">Lanternfly</h2>
    <div class="footer">
      <p class="footer__contact">tallowcreekcoffee.example | 47 Garrick St, Bellwood, NSW</p>
      <p class="footer__origin">Proudly roasted in Bellwood, NSW</p>
    </div>
  </article>

  <article class="label label--slowtide">
    <div class="label__tone"></div>
    <div class="donation">
      <span class="donation__badge">$1</span>
      <p class="donation__text">donated from every kg of coffee sold to fund schooling and safe homes for children in need.</p>
    </div>
    <h1 class="brand"><span class="brand__name">Tallow Creek</span><span class="brand__trade">Coffee Roasters</span></h1>
    <p class="tagline">Roast Kindly | Share Freely | Stay Curious</p>
    <h2 class="blend">Slow Tide</h2>
    <div class="footer">
      <p class="footer__contact">tallowcreekcoffee.example | 47 Garrick St, Bellwood, NSW</p>
      <p class="footer__origin">Proudly roasted in Bellwood, NSW</p>
    </div>
  </article>

</main>
</body>
</html>
```